I need to refresh my meeting minutes pages (2 of them)

I have 2 pages that need to be modernized with a new look and feel. I have attached the 2 pages that need the refresh. I am okay with one page submissions as long as the winner is willing to add the second page before payment :-) Any questions please let me know. The logo on the page is not ours but a sample of what client may give us.

```html
<!DOCTYPE html>
<html lang="en">
<head>
<meta charset="utf-8">
<title>Harbor Lane – Meetings</title>
<link rel="stylesheet" href="https://fonts.googleapis.com/css2?family=Poppins:wght@400;500;600&display=swap">
<style>
:root{
  --blue:#0066ff;
  --navy:#0d3068;
  --ink:#1f2937;
  --muted:#4b5563;
  --page:#f4f7fc;
  --line:#dfe3ea;
  --red:#e11d1d;
  --view-bg:#e6ecfb;
  --pdf:#0c8a72;
  --pdf-bg:#dcf3f0;
  --print:#f6b73c;
  --print-text:#a06a00;
  --print-bg:#fdf3dc;
}
*{box-sizing:border-box;margin:0;padding:0}
html,body{width:1200px;height:1111px;overflow:hidden;background:var(--page)}
body{font-family:"Poppins",sans-serif;color:var(--ink)}
.stage{width:1700px;height:1574px;transform:scale(.70588);transform-origin:0 0;position:relative;background:var(--page)}
.topbar{position:absolute;left:0;top:0;width:1700px;height:89px;background:#fff;box-shadow:0 4px 14px rgba(13,48,104,.06);z-index:2}
.brand{position:absolute;left:20px;top:27px;font-size:25px;font-weight:500;color:var(--blue)}
.search{position:absolute;left:1039px;top:14px;width:601px;height:61px;border:1px solid #b9cdf3;border-radius:8px;background:#eef3fc;display:flex;align-items:center;padding-left:18px;gap:8px;font-size:17px;color:#5b6472}
.sidebar{position:absolute;left:0;top:0;width:477px;height:1503px;background:#fff;border-right:1px solid var(--line)}
.nav{position:absolute;left:19px;top:100px;width:429px}
.nav a{display:block;height:63px;line-height:63px;padding-left:17px;font-size:18px;font-weight:500;color:var(--navy);text-decoration:none;border-radius:8px}
.nav a.active{background:var(--blue);color:#fff;box-shadow:0 4px 10px rgba(0,102,255,.25)}
.year{position:absolute;left:19px;top:357px;width:429px;height:63px;background:var(--navy);border-radius:8px;color:#fff;font-size:20px;line-height:63px;padding-left:17px}
.year .toggle{position:absolute;right:10px;top:13px;width:36px;height:36px;background:#fff;border-radius:6px}
.year .toggle::after{content:"";position:absolute;left:9px;top:16px;width:18px;height:4px;background:var(--navy);border-radius:2px}
.meeting-list{position:absolute;left:36px;top:440px;width:412px;list-style:none}
.meeting-list li{height:81.7px;padding-top:6px;border-bottom:1px solid var(--line)}
.meeting-list li:last-child{border-bottom:none}
.meeting-list .date{font-size:17px;font-weight:600;color:#2a2f38;line-height:28px}
.meeting-list .kind{font-size:17px;color:var(--muted);line-height:28px}
.cancelled{color:var(--red)}
.scroll-thumb{position:absolute;left:473px;top:532px;width:7px;height:73px;background:var(--blue);border-radius:4px}
.card{position:absolute;left:531px;width:1109px;background:#fff;border-radius:14px;box-shadow:0 6px 22px rgba(13,48,104,.06)}
.card-bar{position:absolute;left:18px;top:17px;width:1072px;height:70px;background:var(--blue);border-radius:8px}
.arrow-btn{position:absolute;top:12px;width:46px;height:46px;background:#fff;border-radius:6px;display:flex;align-items:center;justify-content:center}
.share{position:absolute;right:14px;top:18px}
.title{position:absolute;left:37px;font-size:31px;font-weight:500;color:var(--navy)}
.subdate{position:absolute;left:37px;font-size:20px;color:var(--muted)}
.info{position:absolute;left:35px;display:flex;gap:20px}
.info strong{display:block;font-size:20px;font-weight:600;color:#2a2f38;line-height:30px}
.info p{font-size:20px;color:#3a414c;line-height:37px}
.actions{position:absolute;display:flex;gap:24px}
.action{width:296px;height:80px;border-radius:8px;display:flex;align-items:center;gap:20px;padding-left:8px;font-size:19px;font-weight:500;line-height:25px}
.action .ico{width:64px;height:64px;border-radius:8px;display:flex;align-items:center;justify-content:center;flex:none}
.view{background:var(--view-bg);color:var(--blue)}.view .ico{background:var(--blue)}
.pdf{background:var(--pdf-bg);color:var(--pdf)}.pdf .ico{background:var(--pdf)}
.print{background:var(--print-bg);color:var(--print-text)}.print .ico{background:var(--print)}
.footer{position:absolute;left:0;top:1503px;width:1700px;height:71px;background:var(--navy);color:#fff;font-size:19px;text-align:center;line-height:71px}
</style>
</head>
<body>
<div class="stage">
  <aside class="sidebar">
    <nav class="nav">
      <a href="#">FEATURED</a>
      <a href="#" class="active">MEETINGS</a>
      <a href="#">AGENDA</a>
      <a href="#">POLICIES</a>
    </nav>
    <div class="year">2025<span class="toggle"></span></div>
    <ul class="meeting-list">
      <li><div class="date">May 1, 2025 (Thu)</div><div class="kind">Special Meeting Agenda</div></li>
      <li><div class="date">Apr 24, 2025 (Thu)</div><div class="kind">Regular Meeting Agenda</div></li>
      <li><div class="date">Apr 10, 2025 (Thu)</div><div class="kind">Regular Meeting Agenda</div></li>
      <li><div class="date">Mar 20, 2025 (Thu)</div><div class="kind">Regular Meeting Agenda</div></li>
      <li><div class="date">Mar 17, 2025 (Mon)</div><div class="kind">Special Meeting Agenda</div></li>
      <li><div class="date">Mar 12, 2025 (Wed)</div><div class="kind">Special Meeting Agenda</div></li>
      <li><div class="date">Mar 6, 2025 (Thu)</div><div class="kind">Regular Meeting Agenda</div></li>
      <li><div class="date">Feb 26, 2025 (Wed)</div><div class="kind">Special Meeting Agenda <span class="cancelled">Cancelled</span></div></li>
      <li><div class="date">Feb 20, 2025 (Thu)</div><div class="kind">Regular Meeting Agenda</div></li>
      <li><div class="date">Feb 6, 2025 (Thu)</div><div class="kind">Regular Meeting Agenda</div></li>
      <li><div class="date">Feb 3, 2025 (Mon)</div><div class="kind">Special Meeting Agenda</div></li>
      <li><div class="date">Jan 23, 2025 (Thu)</div><div class="kind">Regular Meeting Agenda</div></li>
      <li><div class="date">Jan 14, 2025 (Tue)</div><div class="kind">Special Meeting Agenda</div></li>
    </ul>
  </aside>
  <div class="scroll-thumb"></div>

  <header class="topbar">
    <div class="brand">Harbor Lane</div>
    <div class="search">
      <svg width="26" height="26" viewBox="0 0 24 24" fill="none" stroke="#5b6472" stroke-width="2"><circle cx="10.5" cy="10.5" r="7.5"/><path d="M16 16l5 5" stroke-linecap="round"/></svg>
      Search Agenda
    </div>
  </header>

  <!-- Meeting card 1 -->
  <section class="card" style="top:123px;height:629px">
    <div class="card-bar">
      <span class="arrow-btn" style="left:14px"><svg width="22" height="22" viewBox="0 0 24 24" fill="none" stroke="#111" stroke-width="2.2" stroke-linecap="round" stroke-linejoin="round"><path d="M20 12H4M10 6l-6 6 6 6"/></svg></span>
      <span class="arrow-btn" style="left:69px"><svg width="22" height="22" viewBox="0 0 24 24" fill="none" stroke="#111" stroke-width="2.2" stroke-linecap="round" stroke-linejoin="round"><path d="M4 12h16M14 6l6 6-6 6"/></svg></span>
      <svg class="share" width="34" height="34" viewBox="0 0 24 24" fill="none" stroke="#fff" stroke-width="2.2" stroke-linecap="round" stroke-linejoin="round"><path d="M18 14v5a2 2 0 0 1-2 2H5a2 2 0 0 1-2-2V8a2 2 0 0 1 2-2h4"/><path d="M15 3h6v6M21 3l-9 9"/></svg>
    </div>
    <h2 class="title" style="top:128px">Regular Meeting Agenda</h2>
    <div class="subdate" style="top:175px">Thursday, April 24, 2025</div>
    <div class="info" style="top:227px">
      <svg width="22" height="28" viewBox="0 0 24 30"><path d="M12 0C5.4 0 0 5.2 0 11.7 0 20 12 30 12 30s12-10 12-18.3C24 5.2 18.6 0 12 0z" fill="#0066ff"/><circle cx="12" cy="11" r="4" fill="#fff"/></svg>
      <div><strong>Westbrook High School</strong><p>Media Center 1800 North Maple Ridge Road Lakeview, Ohio 44090</p></div>
    </div>
    <div class="info" style="top:337px">
      <svg width="34" height="34" viewBox="0 0 24 24" fill="none" stroke="#0066ff" stroke-width="2" stroke-linecap="round"><circle cx="12" cy="12" r="9.5" stroke-dasharray="50 6"/><path d="M12 7v5l3 2"/></svg>
      <div style="margin-left:-14px"><strong style="margin-top:2px">6:00 P.M.</strong><p>This Meeting Is A Meeting Of The Board Of Education In Public For The Purpose Of Conducting<br>The District's Business. There Is A Time For Public Participation During The Meetin</p></div>
    </div>
    <div class="actions" style="left:36px;top:508px">
      <a class="action view"><span class="ico"><svg width="40" height="40" viewBox="0 0 40 40" fill="none" stroke="#fff" stroke-width="2.6"><path d="M3 23c5-8 11-11 17-11s12 3 17 11c-5 7-11 10-17 10S8 30 3 23z"/><circle cx="20" cy="23" r="5"/><path d="M14 6l1 3M20 4v4M26 6l-1 3" stroke-linecap="round"/></svg></span>VIEW THE AGENDA</a>
      <a class="action pdf"><span class="ico"><svg width="40" height="42" viewBox="0 0 40 42" fill="none" stroke="#fff" stroke-width="2.4"><path d="M10 12V3h16l6 6v3M10 30v9h22V30"/><rect x="5" y="14" width="30" height="14" rx="2"/><text x="20" y="25.5" fill="#fff" stroke="none" font-family="Poppins,sans-serif" font-size="10" font-weight="600" text-anchor="middle">PDF</text><path d="M21 31v7M18 35l3 3 3-3"/></svg></span>DOWNLOAD<br>AGENDA AS PDF</a>
      <a class="action print"><span class="ico"><svg width="40" height="40" viewBox="0 0 40 40" fill="none" stroke="#fff" stroke-width="2.6"><path d="M11 13V5h18v8"/><rect x="4" y="13" width="32" height="15" rx="3"/><rect x="11" y="23" width="18" height="12"/><path d="M15 28h10M15 32h10"/><circle cx="30" cy="18" r="1" fill="#fff"/></svg></span>PRINT THE AGENDA</a>
    </div>
  </section>

  <!-- Meeting card 2 -->
  <section class="card" style="top:793px;height:470px">
    <div class="card-bar">
      <span class="arrow-btn" style="left:14px"><svg width="22" height="22" viewBox="0 0 24 24" fill="none" stroke="#111" stroke-width="2.2" stroke-linecap="round" stroke-linejoin="round"><path d="M20 12H4M10 6l-6 6 6 6"/></svg></span>
      <span class="arrow-btn" style="left:69px"><svg width="22" height="22" viewBox="0 0 24 24" fill="none" stroke="#111" stroke-width="2.2" stroke-linecap="round" stroke-linejoin="round"><path d="M4 12h16M14 6l6 6-6 6"/></svg></span>
      <svg class="share" width="34" height="34" viewBox="0 0 24 24" fill="none" stroke="#fff" stroke-width="2.2" stroke-linecap="round" stroke-linejoin="round"><path d="M18 14v5a2 2 0 0 1-2 2H5a2 2 0 0 1-2-2V8a2 2 0 0 1 2-2h4"/><path d="M15 3h6v6M21 3l-9 9"/></svg>
    </div>
    <h2 class="title" style="top:128px">Regular Meeting Agenda</h2>
    <div class="subdate" style="top:175px">Thursday, April 24, 2025</div>
    <div class="info" style="top:227px">
      <svg width="22" height="28" viewBox="0 0 24 30"><path d="M12 0C5.4 0 0 5.2 0 11.7 0 20 12 30 12 30s12-10 12-18.3C24 5.2 18.6 0 12 0z" fill="#0066ff"/><circle cx="12" cy="11" r="4" fill="#fff"/></svg>
      <div><strong>Westbrook High School</strong><p>Media Center 1800 North Maple Ridge Road Lakeview, Ohio 44090</p></div>
    </div>
    <div class="actions" style="left:31px;top:336px">
      <a class="action view"><span class="ico"><svg width="40" height="40" viewBox="0 0 40 40" fill="none" stroke="#fff" stroke-width="2.6"><path d="M3 23c5-8 11-11 17-11s12 3 17 11c-5 7-11 10-17 10S8 30 3 23z"/><circle cx="20" cy="23" r="5"/><path d="M14 6l1 3M20 4v4M26 6l-1 3" stroke-linecap="round"/></svg></span>VIEW THE AGENDA</a>
      <a class="action pdf"><span class="ico"><svg width="40" height="42" viewBox="0 0 40 42" fill="none" stroke="#fff" stroke-width="2.4"><path d="M10 12V3h16l6 6v3M10 30v9h22V30"/><rect x="5" y="14" width="30" height="14" rx="2"/><text x="20" y="25.5" fill="#fff" stroke="none" font-family="Poppins,sans-serif" font-size="10" font-weight="600" text-anchor="middle">PDF</text><path d="M21 31v7M18 35l3 3 3-3"/></svg></span>DOWNLOAD<br>AGENDA AS PDF</a>
      <a class="action print"><span class="ico"><svg width="40" height="40" viewBox="0 0 40 40" fill="none" stroke="#fff" stroke-width="2.6"><path d="M11 13V5h18v8"/><rect x="4" y="13" width="32" height="15" rx="3"/><rect x="11" y="23" width="18" height="12"/><path d="M15 28h10M15 32h10"/><circle cx="30" cy="18" r="1" fill="#fff"/></svg></span>PRINT THE AGENDA</a>
    </div>
  </section>

  <footer class="footer">© 2025 HarborLane. All Rights Reserved.</footer>
</div>
</body>
</html>
```